Business Card Design Project

We have a logo, but would like to expand the use of it into a business card design. We are a B2B technology exchange platform for institutional investors to invest excess cash into short term assets matching their credit and pricing parameters. The assets are fractionalized and investors invest in portions.

Our customers are large, institutional, financial companies who are a bit traditional. We are high energy rebels with a cause...we are a disruptive technology and want to be viewed as a game changer but we need to present an image of trustworthiness and secure.

We are open not only to the image design but the material, die cut, etc. but want to stay in the traditional size of a business card.

We have other formats of the logo if needed. Our website is www.brambleharbor.com

I have posted a powerpoint template that we have been using.  This should not be considered the template we will use (after business cards we will have another project to incorporate business card design into powerpoint template) but just to give you a flavor of where we have been and have used in the past.

Target Market(s)

Institutional investors, asset managers, large fund institutions

Industry/Entity Type

Financial

Requirements
Must have
• Our logo
Traditional size
Nice to have
• unique use of logo, unique material, die cut, etc
Crisp, clean look
Use of both sides of card in a creative manner

```html
<!DOCTYPE html>
<html lang="en">
<head>
<meta charset="utf-8">
<title>Bramble Harbor – Business Card</title>
<link rel="stylesheet" href="https://fonts.googleapis.com/css2?family=Montserrat:wght@700&family=Questrial&display=swap">
<style>
  :root {
    --page-bg: #e3e1dd;
    --card-bg: #ededed;
    --brand-orange: #f39220;
    --slate: #606060;
    --ink: #333333;
    --white: #ffffff;
  }
  html, body {
    margin: 0;
    padding: 0;
    width: 1200px;
    height: 801px;
    overflow: hidden;
    background: var(--page-bg);
  }
  .stage {
    position: relative;
    width: 1200px;
    height: 801px;
  }
  .business-card {
    position: absolute;
    left: 100px;
    top: 121px;
    width: 1000px;
    height: 559px;
    box-shadow: 0 6px 18px rgba(0,0,0,0.18);
  }
  .business-card svg { display: block; }
  .card-base { fill: var(--card-bg); }
  .block-orange { fill: var(--brand-orange); }
  .block-slate { fill: var(--slate); }
  .brand-name {
    font-family: "Montserrat", sans-serif;
    font-weight: 700;
    font-size: 27px;
    fill: var(--slate);
    letter-spacing: 0.5px;
  }
  .brand-dot { fill: var(--brand-orange); }
  .person-name {
    font-family: "Montserrat", sans-serif;
    font-weight: 700;
    font-size: 27px;
    fill: var(--white);
  }
  .person-title {
    font-family: "Questrial", sans-serif;
    font-size: 26px;
    fill: var(--white);
  }
  .contact-line {
    font-family: "Questrial", sans-serif;
    font-size: 21px;
    fill: var(--ink);
  }
  .address-line {
    font-family: "Questrial", sans-serif;
    font-size: 16.5px;
    fill: var(--ink);
  }
  .icon {
    fill: none;
    stroke: var(--slate);
    stroke-width: 1.4;
    stroke-linecap: round;
    stroke-linejoin: round;
  }
  .icon-solid { fill: var(--slate); }
</style>
</head>
<body>
<main class="stage">
  <article class="business-card">
    <svg width="1000" height="559" viewBox="0 0 888 496" xmlns="http://www.w3.org/2000/svg">
      <rect class="card-base" x="0" y="0" width="888" height="496"/>

      <!-- colour blocks -->
      <polygon class="block-orange" points="0,0 277,0 299,68 0,165"/>
      <polygon class="block-orange" points="0,362 355,247 435,496 0,496"/>
      <polygon class="block-slate" points="277,0 888,0 888,74 355,247"/>

      <!-- brand name -->
      <g class="brand-lockup" transform="translate(168 216) rotate(-18)">
        <circle class="brand-dot" cx="-142" cy="-9" r="9"/>
        <text class="brand-name" x="-126" y="0">BRAMBLE HARBOR</text>
      </g>

      <!-- name and title -->
      <g class="identity" transform="translate(368 171) rotate(-18)">
        <text class="person-name" x="0" y="0">Marcus Ellery</text>
        <text class="person-title" x="-4" y="41">President &amp; CEO</text>
      </g>

      <!-- contact details -->
      <g class="contact" transform="translate(436 261) rotate(-18)">
        <g class="contact-icons" transform="translate(-28 0)">
          <!-- phone -->
          <path class="icon-solid" d="M-4,-14 l3,-1 2,5 -2,1.5 q1,3.5 4,6 l1.8,-1.6 4,3 -1.5,2.8 q-6,0.5 -10,-6 q-3,-5 -1.3,-9.7z"/>
          <!-- mobile -->
          <rect class="icon" x="-5" y="14" width="10" height="15" rx="1.5"/>
          <line class="icon" x1="-1.5" y1="26" x2="1.5" y2="26"/>
          <!-- envelope -->
          <rect class="icon" x="-7" y="44" width="14" height="9" rx="1"/>
          <polyline class="icon" points="-7,44 0,49.5 7,44"/>
          <!-- globe -->
          <circle class="icon" cx="0" cy="77" r="7"/>
          <ellipse class="icon" cx="0" cy="77" rx="3" ry="7"/>
          <line class="icon" x1="-7" y1="77" x2="7" y2="77"/>
          <!-- profile -->
          <rect class="icon" x="-6.5" y="99" width="13" height="13" rx="2"/>
        </g>
        <text class="contact-line" x="0" y="0">555.214.3380</text>
        <text class="contact-line" x="0" y="28">555.407.9126</text>
        <text class="contact-line" x="0" y="56">marcusellery@brambleharbor.com</text>
        <text class="contact-line" x="0" y="84">www.BrambleHarbor.com</text>
        <text class="contact-line" x="0" y="112">marcusellery</text>

        <g class="address">
          <text class="address-line" x="-37" y="159">2150 Cedar Hollow Drive</text>
          <text class="address-line" x="-37" y="181">Suite 418</text>
          <text class="address-line" x="-37" y="203">Fairmont Springs, CA 90412</text>
        </g>
      </g>
    </svg>
  </article>
</main>
</body>
</html>
```